Letterbox flyer design

Hi - hoping you're able to help design a flyer for letterbox delivery. I think it needs to be 99mm x 210mm.

Side 1 - Large Logo, dark back ground.
Larger text - "5%* Property Management."
Medium Text - "Better Services, Lower Fee's, Higher Yields"
Smaller text at bottom - "0427 519 684 - marcus@kelbridge.com.au - kelbridge.com.au"

Back Side -
• Management Fee – 5%+GST of rent collected (no rent paid = no mgmt. fee charged)
• An Establishment fee of $500 for new tenancies we establish.
• Marketing Costs as Required and agreed to between parties.
• No Fee’s for Condition Reports, inspections, re-listing, tenancy renewal, admin costs, or any other ‘sundry’ charges.
• All rent is paid out monthly, yearly ‘profit-and-loss’ statements at no cost.
• Ingoing condition report is produced prior to occupancy, and routine condition inspections are conducted after the first 3months, then every 6months.
• Open homes are advertised in advance, and held on the weekend and one lunchtime or evening per week.
• All applicants are vetted, with the most suitable sent through for your consideration and approval.
• Advise on different tenancy terms as they could have the ability to affect the long-term yields.

```html
<!DOCTYPE html>
<html lang="en">
<head>
<meta charset="utf-8">
<title>Kelbridge &amp; Co – Letterbox Flyer</title>
<link href="https://fonts.googleapis.com/css2?family=Montserrat:wght@400;700;900&display=swap" rel="stylesheet">
<style>
  :root {
    --backdrop: #b3b1b2;
    --teal: #4ac4d0;
    --ink: #050708;
    --slate: #8a8c8f;
    --white: #ffffff;
  }
  * { margin: 0; padding: 0; box-sizing: border-box; }
  html, body { width: 1200px; height: 1200px; overflow: hidden; }
  body { background: var(--backdrop); position: relative; font-family: "Montserrat", sans-serif; }

  .flyer-side {
    position: absolute; top: 132px; width: 456px; height: 935px;
    overflow: hidden; box-shadow: 0 4px 14px rgba(0,0,0,0.35);
  }
  .flyer-front { left: 104px; background: var(--ink); }
  .flyer-back { left: 638px; background: var(--white); }
  .side-shape { position: absolute; inset: 0; width: 100%; height: 100%; }

  .headline-rate {
    position: absolute; top: 18px; width: 100%; text-align: center;
    font-weight: 900; font-size: 90px; line-height: 1; color: var(--ink); letter-spacing: -2px;
  }
  .headline-service {
    position: absolute; top: 106px; width: 100%; text-align: center;
    font-weight: 700; font-size: 35px; color: var(--white);
  }

  .brand-name {
    position: absolute; font-family: "Montserrat", sans-serif;
    font-weight: 700; color: var(--slate); text-transform: uppercase;
  }
  .brand-name span { display: block; }
  .front-name {
    top: 390px; width: 100%; text-align: center;
    font-size: 32px; line-height: 44px;
  }
  .back-name {
    top: 838px; width: 100%; text-align: center;
    font-size: 24px; line-height: 32px;
  }

  .tagline {
    position: absolute; top: 652px; width: 100%; text-align: center;
    color: var(--teal); font-size: 30px; line-height: 37px; font-weight: 400;
  }

  .contact-divider {
    position: absolute; top: 808px; left: 95px; width: 266px; height: 22px;
    display: flex; align-items: center; justify-content: space-between;
  }
  .divider-rule { width: 70px; height: 2px; background: var(--teal); }
  .contact-icons { display: flex; gap: 9px; }
  .contact-icon { width: 22px; height: 22px; }

  .contact-list {
    position: absolute; top: 838px; width: 100%; text-align: center;
    color: var(--white); font-size: 18.5px; line-height: 24.5px; list-style: none;
  }

  .service-list {
    position: absolute; top: 21px; left: 47px; width: 382px; list-style: none;
    font-size: 17px; line-height: 24.4px; color: var(--ink);
  }
  .service-list li { position: relative; margin-bottom: 10.5px; }
  .service-list li::before {
    content: ""; position: absolute; left: -19px; top: 8px;
    width: 9px; height: 9px; border-radius: 50%; background: var(--teal);
  }
  .service-list strong { font-weight: 700; }
</style>
</head>
<body>

<section class="flyer-side flyer-front">
  <svg class="side-shape" viewBox="0 0 456 935" preserveAspectRatio="none" aria-hidden="true">
    <path d="M0 166 Q228 290 456 144 L456 0 L0 0 Z" fill="var(--slate)"/>
    <path d="M0 132 Q228 265 456 140 L456 0 L0 0 Z" fill="var(--teal)"/>
  </svg>
  <div class="headline-rate">5%*</div>
  <div class="headline-service">Property Management</div>

  <div class="brand-name front-name">
    <span>Kelbridge &amp; Co</span>
    <span>Property Services</span>
  </div>

  <p class="tagline">Better Services,<br>Lower Fee's,<br>Higher Yields</p>

  <div class="contact-divider">
    <span class="divider-rule"></span>
    <span class="contact-icons">
      <svg class="contact-icon" viewBox="0 0 22 22" aria-label="Phone">
        <circle cx="11" cy="11" r="10" fill="none" stroke="var(--teal)" stroke-width="1.3"/>
        <path d="M7.5 6.5 L9.5 6.3 L10.3 8.6 L9.2 9.5 Q10.2 11.8 12.5 12.8 L13.4 11.7 L15.7 12.5 L15.5 14.5 Q10 15 7.5 6.5 Z" fill="none" stroke="var(--white)" stroke-width="1.1"/>
      </svg>
      <svg class="contact-icon" viewBox="0 0 22 22" aria-label="Email">
        <circle cx="11" cy="11" r="10" fill="none" stroke="var(--teal)" stroke-width="1.3"/>
        <rect x="6" y="7.5" width="10" height="7" fill="none" stroke="var(--white)" stroke-width="1.1"/>
        <path d="M6 7.5 L11 11.5 L16 7.5 M6 14.5 L9.5 11 M16 14.5 L12.5 11" fill="none" stroke="var(--white)" stroke-width="1.1"/>
      </svg>
      <svg class="contact-icon" viewBox="0 0 22 22" aria-label="Website">
        <circle cx="11" cy="11" r="10" fill="none" stroke="var(--teal)" stroke-width="1.3"/>
        <circle cx="11" cy="11" r="5" fill="none" stroke="var(--white)" stroke-width="1.1"/>
        <path d="M6 11 H16 M11 6 V16 M11 6 Q8 11 11 16 M11 6 Q14 11 11 16" fill="none" stroke="var(--white)" stroke-width="1"/>
      </svg>
    </span>
    <span class="divider-rule"></span>
  </div>

  <ul class="contact-list">
    <li>0427 519 684</li>
    <li>marcus@kelbridge.com.au</li>
    <li>kelbridge.com.au</li>
  </ul>
</section>

<section class="flyer-side flyer-back">
  <ul class="service-list">
    <li><strong>Management Fee – 5%+GST</strong> of rent collected (no rent paid = no mgmt. fee charged).</li>
    <li><strong>An Establishment fee of $500</strong> for new tenancies we establish.</li>
    <li><strong>Marketing Costs as Required</strong> and agreed to between parties.</li>
    <li><strong>No Fee’s for Condition Reports</strong>, inspections, re-listing, tenancy renewal, admin costs, or any other ‘sundry’ charges.</li>
    <li><strong>All rent is paid out</strong> monthly, yearly ‘profit-and-loss’ statements at no cost.</li>
    <li><strong>Ingoing condition report is produced</strong> prior to occupancy, and routine condition inspections are conducted after the first 3months, then every 6months.</li>
    <li><strong>Open homes are advertised</strong> in advance, and held on the weekend and one lunchtime or evening per week.</li>
    <li><strong>All applicants are vetted</strong>, with the most suitable sent through for your consideration and approval.</li>
    <li><strong>Advise on different tenancy terms</strong> as they could have the ability to affect the long-term yields.</li>
  </ul>

  <svg class="side-shape" viewBox="0 0 456 935" preserveAspectRatio="none" aria-hidden="true">
    <path d="M0 781 Q228 640 456 765 L456 935 L0 935 Z" fill="var(--teal)"/>
    <path d="M0 799 Q228 665 456 805 L456 935 L0 935 Z" fill="var(--ink)"/>
  </svg>

  <div class="brand-name back-name">
    <span>Kelbridge &amp; Co</span>
    <span>Property Services</span>
  </div>
</section>

</body>
</html>
```